RideMatcher.net

We require the look and feel creating for a new website which will allow customers to request & compare airport to resort transport transfers.
The design can be delivered as a one page graphic which our developer will use as a brief when building the website.
Resort destinations would include beach, city & ski.
The above elements should appear in the masthead.
We will also require a logo creating for the site, *perhaps* combing the company name (ridematcher.net) with a car, minibus & aeroplane along with our strapline "Journey on a Budget".
Key phrases which illustrate the type of design we would like are;
Clean, simple, playful, icons (clipart style), professional, bright, big\bold call to action
A few sites we like are;
http://www.pelmotrucks.example/
- especially the clean, playful icons under "Our Services" on the home page
http://www.quotewisp.example/
- but not the background photo!
http://www.lakeshuttlo.example/
a competitor - we feel the homepage is too busy
http://www.artfolkhub.example/
Large icons, clean and clear design.
The site should be 960px wide and centered on the page.
Our developer will use your design to create a flexible bootstrap mobile friendly site using html, css, jquery with a c# mvc mssql backend.
The page should include additional standard\common html elements such as a form, list, div, h1, h2, paragraph etc. This will form the corporate design guidelines for future pages the developer may be asked to create.
Reason: Loving the designs, just need a few more options and streamlining - making this payment guaranteed project because we love the responses so far and looking forward to choosing one of your designs.
Reason: Developer currently away so need to extend until returns to office to decide on a design.
Holiday makers making independent travel arrangements
Building

```html
<!DOCTYPE html>
<html lang="en">
<head>
<meta charset="utf-8">
<title>RideMatcher.net</title>
<link href="https://fonts.googleapis.com/css2?family=Ubuntu:ital,wght@0,300;0,400;0,500;0,700;1,400&display=swap" rel="stylesheet">
<style>
:root{
  --teal:#1f9f82;
  --teal-dark:#17866d;
  --orange:#f7630c;
  --orange-edge:#e0520a;
  --ink:#3b4150;
  --text:#7f8894;
  --heading:#6c7480;
  --page:#fbfdfd;
  --panel:#d8dee5;
  --rule:#dfe3e8;
}
*{box-sizing:border-box;margin:0;padding:0}
html,body{width:1024px;height:1200px;overflow:hidden}
body{position:relative;background:var(--page);font-family:'Ubuntu',sans-serif;color:var(--text)}
.abs{position:absolute}

/* header */
.brand{left:137px;top:36px;display:flex;align-items:flex-start;gap:8px}
.brand-mark{width:32px;height:32px;border-radius:50%;background:#a9adb2;margin-top:2px}
.brand-name{font-size:21px;color:var(--teal);font-weight:400;line-height:1}
.brand-tag{font-size:10px;font-style:italic;color:#8a9098;margin-top:6px;margin-left:2px}
.callus{right:140px;top:30px;font-size:13px;color:#8a9098;display:flex;align-items:center;gap:5px}
.callus b{color:var(--teal);font-weight:500}
.nav{right:141px;top:62px;font-size:13px;color:var(--teal);letter-spacing:.3px}
.nav span{margin:0 7px;color:var(--teal)}

/* hero */
.hero{left:0;top:119px;width:1024px;height:402px;
  background:linear-gradient(180deg,#8fc3bb 0%,#b9c6ae 18%,#d5c29e 45%,#d9c3a3 70%,#c9a99a 100%)}
.transfer-bar{left:135px;top:156px;width:753px;height:40px;background:var(--teal);display:flex;align-items:center}
.transfer-bar h1{font-size:19px;font-weight:400;color:#fff;margin-left:60px;width:228px}
.field{height:25px;background:#fff;border:1px solid #cfd6d8;font-size:11px;color:#9aa1a8;padding:5px 8px}
.from{width:164px}.to{width:164px;margin-left:12px}
.date{width:93px;margin-left:16px;color:#333;font-size:9.5px;display:flex;align-items:center;gap:4px}
.card{top:218px;width:366px;height:220px;background:#fff}
.card h2{position:absolute;left:28px;top:70px;font-size:19px;font-weight:400;color:var(--teal)}
.card .sub{position:absolute;left:28px;top:97px;font-size:9.5px;color:#8a9098}
.btn-want{position:absolute;left:27px;top:131px;width:112px;height:36px;background:var(--orange);border:1px solid var(--orange-edge);color:#fff;font-size:12.5px;font-weight:500;display:flex;align-items:center;justify-content:center}
.vehicle{position:absolute;top:30px;width:175px;height:170px;border-radius:14px;background:linear-gradient(160deg,#e6e8ea,#8c9095)}
.eco{left:138px}.eco .vehicle{left:190px}
.private{left:519px}.private .vehicle{left:178px;background:linear-gradient(160deg,#d0d2d4,#2b2d30)}

/* content */
.section-title{font-size:14px;color:var(--heading);font-weight:400;letter-spacing:.3px}
.list{left:145px;top:582px;list-style:none}
.list li{display:flex;align-items:center;height:28.6px;font-size:11px;color:var(--text)}
.list .tick{width:17px;height:17px;background:var(--teal);margin-right:15px;display:flex;align-items:center;justify-content:center}
.rule{height:4px;border-top:1px solid var(--rule);border-bottom:1px solid var(--rule)}
.contact input,.contact .msg{position:absolute;left:143px;width:365px;background:var(--ink);border:0;color:#b5bbc4;font:11px 'Ubuntu',sans-serif;padding:0 16px}
.send{left:398px;top:1086px;width:112px;height:32px;background:var(--orange);color:#fff;font-size:11.5px;display:flex;align-items:center;justify-content:center;gap:6px}
.page-shot{left:527px;top:597px;width:348px;height:133px;background:var(--panel)}
.page-title{left:525px;top:751px;font-size:14px;color:#4b5160;font-weight:400}
.body-copy{left:527px;top:786px;width:350px;font-size:10.8px;line-height:17.6px;color:var(--text)}
.bq-title{left:529px;top:937px;font-size:13px;font-weight:500;color:var(--heading);letter-spacing:.3px}
blockquote{position:absolute;left:529px;top:972px;width:355px;border-left:3px solid var(--rule);padding-left:16px;font-size:10.5px;line-height:17.4px;color:var(--text)}

/* footer */
.footer{left:0;top:1162px;width:1024px;height:38px;background:linear-gradient(180deg,#e7e9ec,#c9ccd1);border-top:1px solid #b8bcc2;font-size:8.5px;color:#6b717a}
.footer .copy{position:absolute;left:135px;top:13px}
.footer .links{position:absolute;right:137px;top:13px}
.footer .links span{margin:0 8px}
</style>
</head>
<body>

<header>
  <div class="abs brand">
    <div class="brand-mark"></div>
    <div>
      <div class="brand-name">RideMatcher.net</div>
      <div class="brand-tag">Journey on a Budget</div>
    </div>
  </div>
  <div class="abs callus">
    <svg width="19" height="19" viewBox="0 0 19 19"><rect width="19" height="19" rx="3" fill="#a9adb2"/><path d="M6 4.5c-1 .5-1.5 1.5-1 3 1 3 3.5 5.5 6.5 6.5 1.5.5 2.5 0 3-1l-2-2-1.5 1c-1.5-.7-2.8-2-3.5-3.5l1-1.5z" fill="#fff"/></svg>
    Call us today <b>+1800.555.0199</b>
  </div>
  <nav class="abs nav">HOME<span>|</span>ABOUT<span>|</span>CONTACT</nav>
</header>

<section>
  <div class="abs hero" role="img" aria-label="Blurred photo of a busy sunny beach with colourful umbrellas and towels"></div>
  <div class="abs transfer-bar">
    <h1>I want to transfer...</h1>
    <div class="field from">From</div>
    <div class="field to">To</div>
    <div class="field date">
      <svg width="11" height="11" viewBox="0 0 11 11"><rect x="0.5" y="1.5" width="10" height="9" fill="none" stroke="#333"/><rect x="0.5" y="1.5" width="10" height="2.5" fill="#333"/><rect x="2.5" y="0" width="1" height="2.5" fill="#333"/><rect x="7.5" y="0" width="1" height="2.5" fill="#333"/></svg>
      3 / 10 / 2013
    </div>
  </div>
  <div class="abs card eco">
    <h2>Eco Transfer</h2>
    <div class="sub">A SHARED TRANSFER</div>
    <div class="btn-want">I want this</div>
    <div class="vehicle" role="img" aria-label="White shuttle bus"></div>
  </div>
  <div class="abs card private">
    <h2>Private Transfer</h2>
    <div class="sub">ONE CLIENT ONLY</div>
    <div class="btn-want">I want this</div>
    <div class="vehicle" role="img" aria-label="Black taxi car"></div>
  </div>
</section>

<main>
  <h3 class="abs section-title" style="left:145px;top:557px">LIST 1</h3>
  <ul class="abs list">
    <li><span class="tick"><svg width="6" height="8" viewBox="0 0 6 8"><path d="M1 1l3 3-3 3" stroke="#fff" stroke-width="1.6" fill="none"/></svg></span>Le Aorem Ipsum ainsi obtenu ne contient aucune</li>
    <li><span class="tick"><svg width="6" height="8" viewBox="0 0 6 8"><path d="M1 1l3 3-3 3" stroke="#fff" stroke-width="1.6" fill="none"/></svg></span>répétition secolilorem nunc.adipiscing</li>
    <li><span class="tick"><svg width="6" height="8" viewBox="0 0 6 8"><path d="M1 1l3 3-3 3" stroke="#fff" stroke-width="1.6" fill="none"/></svg></span>Contrairement à une opinion répandue, le Lorem</li>
    <li><span class="tick"><svg width="6" height="8" viewBox="0 0 6 8"><path d="M1 1l3 3-3 3" stroke="#fff" stroke-width="1.6" fill="none"/></svg></span>Ipsum n'est pas at erat in purus aliquet</li>
    <li><span class="tick"><svg width="6" height="8" viewBox="0 0 6 8"><path d="M1 1l3 3-3 3" stroke="#fff" stroke-width="1.6" fill="none"/></svg></span>On sait depuis longtemps que travailler avec du texte</li>
    <li><span class="tick"><svg width="6" height="8" viewBox="0 0 6 8"><path d="M1 1l3 3-3 3" stroke="#fff" stroke-width="1.6" fill="none"/></svg></span>lisible quanto contrairement à une</li>
  </ul>
  <div class="abs rule" style="left:145px;top:765px;width:296px"></div>

  <form class="contact">
    <h3 class="abs section-title" style="left:143px;top:805px">CONTACT FORM</h3>
    <input type="text" placeholder="Name" style="top:842px;height:40px">
    <input type="email" placeholder="Email address" style="top:898px;height:40px">
    <div class="msg" style="top:956px;height:114px;padding-top:14px">Massage</div>
    <p class="abs" style="left:143px;top:1096px;font-size:11px">Email will never be published!</p>
    <div class="abs send">Send message
      <svg width="11" height="9" viewBox="0 0 11 9"><path d="M1 4.5l3 3 6-6" stroke="#fff" stroke-width="2" fill="none"/></svg>
    </div>
  </form>

  <h3 class="abs section-title" style="left:527px;top:559px">PAGE STYLE</h3>
  <div class="abs page-shot"></div>
  <h2 class="abs page-title">Title of Page</h2>
  <p class="abs body-copy">OT Porta montes montes vel nunc cras porttitor mid elementum dictumst dignissim dapibusurna ac, enim? Porttitor! Aenean, urna, magna dictumst odio massa in in risus nunc auguephasellus mattis mid elementum dictumst dignissim dapibus urna ac, enim? Porttitor! Aenean,urna, magna dictumst odio, a tincidunt rhoncus massa in in risus nunc augue phasellus mattisAenean, urna, magna dictumst odio massa in in risus nunc augue phasellus mattis midelementum</p>
  <h3 class="abs bq-title">BLOCKQUOTE</h3>
  <blockquote>Cras consequat porttitor tincidunt. Praesent eu tincidunt lacus. Donec ut neque vitae eratcongue venenatis. Duis hendrerit lacinia leo in dignissim. Aliquam erat volutpat. Seddignissim hendrerit nibh, quis faucibus erat cursus eget. Integer porta nisl vitae felis rutrum</blockquote>
  <div class="abs rule" style="left:528px;top:1059px;width:362px"></div>
</main>

<footer class="abs footer">
  <div class="copy">Copyright 2014 © CompanyName - All Rights Reserved</div>
  <div class="links">Site Map<span>•</span>Privacy Policy</div>
</footer>

</body>
</html>
```